Sunbirds Postcard .psd

Please supply a print-ready layered .psd file
- 148mm wide x 105mm deep with 3mm bleed
- CMYK for gloss card

Target Market(s)

Women 25 - 40

Requirements
Must have
• Fun look - heart (casually drawn) - writing (sketch look/feel) in the background and faded to say "Love is patient and kind. Love is not jealous or boastful or proud or rude. It does not demand its own way. It is not irritable, and it keeps no record of being wronged. It does not rejoice about injustice but rejoices whenever the truth wins out. Love never gives up, never loses faith, is always hopeful, and endures through every circumstance."

images/text overlay for the front in bold colour (almost like being branded / tattooed / stamp / seal)

Text:
Front: Chosen and marked by Love (emphasise love)
Sunbirds logo (attached - use in any colour)

Back: Save the dates: 6 March, 29 May, 14 August, 27 November
Cost: $10 each event
Time: 7:00pm
Location: The Marlow, 412 Brindle St, Newcastle 2300
These events are hosted by Chapel247 to enable women across the region to inspire and encourage others to make a difference in their relationships and world. Our heart is that we as women develop a deep abiding peace, acceptance and experience the overwhelming embracing love of God.
Chapel247 Logo (attached)
Nice to have
• pictures of Women having fun / laughing (can get from PixVault - please use low res version until approved and then I will purchase).

See examples given of type (type.jpg) and background text (text.jpg)
Should not have
• not women posing for pictures, smiling at the camera

```html
<!DOCTYPE html>
<html lang="en">
<head>
<meta charset="utf-8">
<title>Sunbirds – Save the Dates</title>
<link rel="stylesheet" href="https://fonts.googleapis.com/css2?family=Della+Respira&family=Kalam:wght@700&display=swap">
<style>
  :root {
    --paper: #ffffff;
    --ink: #1a1a1a;
    --brand-grey: #8c8c8c;
  }
  html, body {
    margin: 0;
    padding: 0;
    width: 1200px;
    height: 851px;
    overflow: hidden;
    background: var(--paper);
  }
  .postcard-back {
    position: relative;
    width: 1200px;
    height: 851px;
    background: var(--paper);
    color: var(--ink);
    font-family: "Della Respira", serif;
    overflow: hidden;
  }
  .brand-wordmark {
    position: absolute;
    left: 110px;
    top: 395px;
    font-family: "Della Respira", serif;
    font-size: 250px;
    line-height: 1;
    color: var(--brand-grey);
    letter-spacing: 4px;
    z-index: 0;
    white-space: nowrap;
  }
  .line {
    position: absolute;
    left: 58px;
    margin: 0;
    white-space: nowrap;
    z-index: 1;
    line-height: 1;
  }
  .detail { font-size: 29px; }
  .detail strong, .emph-bold {
    font-family: "Kalam", cursive;
    font-weight: 700;
  }
  .detail-dates  { top: 48px; }
  .detail-cost   { top: 116px; }
  .detail-time   { top: 176px; }
  .detail-venue  { top: 236px; }
  .detail strong { font-size: 38px; }

  .mission { font-size: 30px; }
  .mission .big { font-size: 50px; }
  .mission .huge { font-size: 54px; }
  .mission .small { font-size: 26px; }
  .mission-1 { top: 340px; }
  .mission-2 { top: 425px; }
  .mission-3 { top: 503px; }
  .mission-4 { top: 588px; }
  .mission-5 { top: 672px; }
  .mission-6 { top: 748px; }
  .host-name {
    font-family: "Della Respira", serif;
    font-size: 38px;
    color: var(--ink);
    letter-spacing: 1px;
  }
  .emph-bold { font-size: 46px; }
</style>
</head>
<body>
<main class="postcard-back">
  <div class="brand-wordmark" aria-hidden="true">sunbirds</div>

  <p class="line detail detail-dates">Save the dates: <strong>6 March</strong>, <strong>29 May</strong>, <strong>14 August</strong>, <strong>27 November</strong></p>
  <p class="line detail detail-cost">Cost: $10 each event</p>
  <p class="line detail detail-time">Time: <strong>7:00pm</strong></p>
  <p class="line detail detail-venue">Location: <strong>The Marlow, 412 Brindle St, Newcastle 2300</strong></p>

  <p class="line mission mission-1">These events are hosted by <span class="host-name">Chapel247</span> to enable <span class="big">women</span></p>
  <p class="line mission mission-2">across the region to <span class="big">inspire</span> and <span class="big">encourage others</span> to</p>
  <p class="line mission mission-3"><span class="big">make a difference</span> <span class="small">in their relationships and world.</span></p>
  <p class="line mission mission-4"><span class="small">Our heart is that we as women develop</span> <span class="big">a deep abiding peace,</span></p>
  <p class="line mission mission-5"><span class="big">acceptance</span> and experience</p>
  <p class="line mission mission-6"><span class="huge">the overwhelming</span> <span class="emph-bold">embracing love of God</span><span class="huge">.</span></p>
</main>
</body>
</html>
```